Harborline Wellness Partners

Please design a business card that is colorful but at the same time easy to read. We are based out on Miami Florida. We are a small start up healthcare company that has been in operation for 1 year. Our clients are Hospitals, Insurance companies, and Manage Care health companies. We are growing quickly and lead the niche we are in. Please make the card 2 sided on the front will be the typical info. Logo, Company Name, Persons Name, Title, Cell #, Office #, Fax#, email, website. No address. On the back we will list 5 services that we do. For example Care Transitions, Case management, Risk assessment, Utilization Review.
Target Market(s)
CEO's and COO's of hospitals and healthcare companies.
Industry/Entity Type
Healthcare

```html
<!DOCTYPE html>
<html lang="en">
<head>
<meta charset="utf-8">
<title>Harborline Wellness Partners – Business Card</title>
<link href="https://fonts.googleapis.com/css2?family=Lato:ital,wght@0,400;0,700;0,900;1,700&display=swap" rel="stylesheet">
<style>
  :root {
    --backdrop: #3a3b3d;
    --card: #ffffff;
    --brand-blue: #1d4fa3;
    --label-blue: #1f5fb0;
    --name-green: #1aa04a;
    --ink: #1c1c1c;
    --logo-grey: #4b4b4f;
    --accent-soft: #4aa8e0;
  }
  * { box-sizing: border-box; margin: 0; padding: 0; }
  html, body { width: 1200px; height: 926px; overflow: hidden; }
  body {
    background: var(--backdrop);
    font-family: "Lato", sans-serif;
    position: relative;
  }
  .card {
    position: absolute;
    left: 260px;
    width: 680px;
    height: 389px;
    background: var(--card);
    overflow: hidden;
    box-shadow: 0 10px 30px rgba(0,0,0,.35);
  }
  .card--back { top: 54px; }
  .card--front { top: 483px; }

  /* Back side */
  .logo {
    position: absolute;
    left: 190px;
    top: 60px;
    display: flex;
    align-items: center;
    gap: 26px;
  }
  .logo__dot {
    width: 110px;
    height: 110px;
    border-radius: 50%;
    background: var(--brand-blue);
  }
  .logo__name {
    font-weight: 900;
    font-size: 38px;
    line-height: 1.12;
    color: var(--logo-grey);
  }
  .services {
    position: absolute;
    left: 0; right: 0; bottom: 0;
    height: 120px;
    background: var(--brand-blue);
    color: #fff;
    display: flex;
    align-items: center;
    justify-content: center;
    text-align: center;
    font-size: 20px;
    letter-spacing: 1.5px;
    line-height: 1.35;
    text-transform: uppercase;
    padding: 0 40px;
  }

  /* Front side */
  .front__band {
    height: 78px;
    background: var(--brand-blue);
    color: #fff;
    font-size: 27px;
    font-weight: 700;
    letter-spacing: 1px;
    padding: 22px 0 0 38px;
    text-transform: uppercase;
  }
  .front__band small { font-size: 22px; font-weight: 400; text-transform: none; }
  .person {
    position: absolute;
    left: 48px;
    top: 112px;
    color: var(--name-green);
    font-size: 36px;
  }
  .person__first { font-weight: 400; }
  .person__last { font-weight: 700; }
  .person__title {
    color: var(--ink);
    font-size: 20px;
    font-weight: 900;
  }
  .contacts {
    position: absolute;
    left: 42px;
    top: 172px;
    list-style: none;
    font-size: 20px;
    line-height: 1.38;
    color: var(--ink);
  }
  .contacts__label {
    color: var(--label-blue);
    font-weight: 700;
    font-style: italic;
  }
  .front__accent {
    position: absolute;
    right: -70px;
    top: 120px;
    width: 330px;
    height: 330px;
    border-radius: 50%;
    background: radial-gradient(circle at 40% 35%, var(--accent-soft), var(--brand-blue));
  }
</style>
</head>
<body>
  <section class="card card--back" aria-label="Business card back">
    <div class="logo">
      <div class="logo__dot"></div>
      <div class="logo__name">Harborline<br>Wellness<br>Partners</div>
    </div>
    <div class="services">
      Care transitions, case management,<br>risk assessment, utilization review and manage care
    </div>
  </section>

  <section class="card card--front" aria-label="Business card front">
    <div class="front__band">Harborline Wellness <small>Partners</small></div>
    <p class="person">
      <span class="person__first">John</span> <span class="person__last">Smith</span>
      <span class="person__title">-TITLE</span>
    </p>
    <ul class="contacts">
      <li><span class="contacts__label">cell:</span> 123-456-7890</li>
      <li><span class="contacts__label">office:</span> 098-765-4321</li>
      <li><span class="contacts__label">fax:</span> 123-098-4567</li>
      <li><span class="contacts__label">email:</span> yourdomain.com</li>
      <li><span class="contacts__label">web:</span> yourname@yourdomain.com</li>
    </ul>
    <div class="front__accent"></div>
  </section>
</body>
</html>
```